Need help in designing new business card utilizing our new logo.

BuildMarq Solutions works with Construction Business Owners, Managers & IT Professionals to strengthen software usage and increase user productivity.

Our Construction Accounting and Mobile Field Management Software Clients engage with us in the following areas:

New Software Implementations
Software Re-Implementations
Redesigning Software Usage at the User Level
Project Coordination & Management
Continued Software Support

Old tag line:
Weighing Options - Implementing Solutions

www.buildmarq-solutions.example

Stride 4 is a product, but not needed for a new business card.

```html
<!DOCTYPE html>
<html lang="en">
<head>
<meta charset="utf-8">
<title>BuildMarq Solutions – Business Card</title>
<link href="https://fonts.googleapis.com/css2?family=Montserrat:wght@400;500&family=Oswald:wght@600&display=swap" rel="stylesheet">
<style>
  :root {
    --backdrop: #161616;
    --card: #242424;
    --card-edge: #2c2c2c;
    --accent: #2e36b0;
    --ink: #f2f2f2;
    --logo-ink: #c9c9c9;
  }
  * { margin: 0; padding: 0; box-sizing: border-box; }
  html, body { width: 1200px; height: 900px; overflow: hidden; }
  body {
    background: var(--backdrop);
    font-family: "Montserrat", sans-serif;
    color: var(--ink);
  }
  .canvas {
    width: 1200px; height: 900px;
    display: flex; flex-direction: column;
    align-items: center; justify-content: center; gap: 40px;
  }
  .card {
    position: relative;
    width: 700px; height: 400px;
    background: linear-gradient(135deg, var(--card-edge), var(--card));
    border-bottom: 7px solid var(--accent);
    box-shadow: 0 10px 30px rgba(0,0,0,.55);
    overflow: hidden;
  }
  /* front */
  .card-front { display: flex; align-items: center; justify-content: center; }
  .brand { display: flex; align-items: center; gap: 18px; }
  .brand-mark { width: 26px; height: 26px; background: var(--logo-ink); }
  .brand-name {
    font-family: "Montserrat", sans-serif; font-weight: 500;
    font-size: 40px; letter-spacing: 1px; color: var(--logo-ink);
  }
  /* back */
  .details {
    position: absolute; left: 44px; right: 30px; top: 118px;
    display: flex; align-items: stretch; gap: 22px;
  }
  .identity {
    flex: none;
    padding-right: 20px; border-right: 2px solid var(--accent);
    text-align: right;
  }
  .person-name {
    font-family: "Oswald", sans-serif; font-weight: 600;
    font-size: 34px; line-height: 1.1; color: var(--accent);
    text-transform: uppercase; text-align: left; white-space: nowrap;
  }
  .person-role { font-size: 17px; margin-top: 4px; }
  .contacts {
    list-style: none; font-size: 15px; line-height: 1.6;
    min-width: 0;
  }
  .contacts li { display: flex; align-items: center; gap: 10px; white-space: nowrap; }
  .contacts svg { width: 13px; height: 13px; flex: none; }
  .address {
    position: absolute; left: 44px; bottom: 46px;
    font-size: 18px;
  }
</style>
</head>
<body>
<main class="canvas">
  <section class="card card-front">
    <div class="brand">
      <span class="brand-mark"></span>
      <span class="brand-name">BuildMarq Solutions</span>
    </div>
  </section>

  <section class="card card-back">
    <div class="details">
      <div class="identity">
        <h1 class="person-name">Dana R. Whitlow</h1>
        <p class="person-role">Owner</p>
      </div>
      <ul class="contacts">
        <li>
          <svg viewBox="0 0 16 16" fill="none" stroke="#2e36b0" stroke-width="1.6"><path d="M4 2l2.5 3-1.5 1.5a8 8 0 0 0 4.5 4.5L11 9.5l3 2.5-1.5 2A10 10 0 0 1 2 3.5z"/></svg>
          800-555-0142 ext.100
        </li>
        <li>
          <svg viewBox="0 0 16 16" fill="none" stroke="#2e36b0" stroke-width="1.6"><rect x="4" y="1.5" width="8" height="13" rx="1.5"/><line x1="7" y1="12" x2="9" y2="12"/></svg>
          518-555-0193
        </li>
        <li>
          <svg viewBox="0 0 16 16" fill="none" stroke="#2e36b0" stroke-width="1.6"><rect x="1.5" y="3.5" width="13" height="9"/><path d="M1.5 3.5L8 9l6.5-5.5"/></svg>
          dana@buildmarq-solutions.example
        </li>
        <li>
          <svg viewBox="0 0 16 16" fill="none" stroke="#2e36b0" stroke-width="1.4"><circle cx="8" cy="8" r="6.5"/><ellipse cx="8" cy="8" rx="3" ry="6.5"/><line x1="1.5" y1="8" x2="14.5" y2="8"/></svg>
          www.buildmarq-solutions.example
        </li>
      </ul>
    </div>
    <p class="address">14B Foundry Lane - Suite 210 Riverton NY 12000</p>
  </section>
</main>
</body>
</html>
```